Design of a Job Advert to inspire people to join our movement

I am looking for a very cool ad to be designed to attract staff to a company. the ad needs to The key objective of this advertisement is to attract Co-creators to join our movement and get an equity share in the platform.

We need to be daring and creative and really get the attention of quality capable resources that can help us to co-create our platform. Which aligns directly with the structure of the company.

The advertisement needs to be very exciting and eye catching. There are key messages that we need to be shown very clearly and needs to pop off the page.

I have attached the ad with all the text changes also I have attached a document that shows the key messages.

I have also included some images from the app for you to use if you feel they will add value.

Can you design an ad that would inspire you personally to be curious to investigate what it is all about.

Something very visually inspiring that is easy to read the key messages.
I will leave it your creative licence.

Thanks and really look forward to seeing the next iteration

Regards Marta

Target Market(s)

Poeple who work for oVex

Requirements
Must have
• Very catching and emotive to move people to understand our movement and join us

```html
<!DOCTYPE html>
<html lang="en">
<head>
<meta charset="utf-8">
<title>Aerolume – Join the Movement</title>
<link href="https://fonts.googleapis.com/css2?family=Bebas+Neue&family=Roboto+Condensed:wght@400&display=swap" rel="stylesheet">
<style>
  :root {
    --blue: #1ba3c6;
    --blue-deep: #168fb0;
    --yellow: #f8cb15;
    --ink: #1b1b1b;
    --paper: #ffffff;
    --backdrop: #e8e8e8;
    --line: #1ba3c6;
  }
  * { margin: 0; padding: 0; box-sizing: border-box; }
  html, body { width: 1200px; height: 592px; overflow: hidden; background: var(--backdrop); }
  .advert {
    position: absolute; left: 391px; top: 0; width: 418px; height: 592px;
    background: var(--paper); overflow: hidden;
    font-family: "Roboto Condensed", sans-serif; color: var(--ink);
  }
  .header-band { position: absolute; left: 0; top: 0; width: 418px; height: 108px; }
  .headline {
    position: absolute; right: 16px; top: 16px; width: 260px; text-align: right;
    font-family: "Bebas Neue", sans-serif; font-weight: 400; font-size: 26px; line-height: 24px;
    color: var(--paper); text-transform: uppercase; white-space: nowrap;
  }
  .brand { position: absolute; left: 14px; top: 42px; display: flex; align-items: center; gap: 6px; }
  .brand-dot { width: 18px; height: 18px; border-radius: 50%; background: var(--blue); }
  .brand-name {
    font-family: "Bebas Neue", sans-serif; font-weight: 400; font-size: 22px;
    letter-spacing: 1.5px; color: var(--yellow);
  }
  .intro {
    position: absolute; left: 14px; right: 14px; top: 151px; text-align: center;
    font-size: 11.5px; line-height: 14px;
  }
  .community-band {
    position: absolute; left: 0; top: 190px; width: 418px; height: 24px;
    background: var(--yellow); text-align: center;
    font-family: "Bebas Neue", sans-serif; font-weight: 400; font-size: 23px; line-height: 25px;
    text-transform: uppercase;
  }
  .app-screens {
    position: absolute; left: 95px; top: 222px; width: 216px; height: 196px;
    border-radius: 14px;
    background: linear-gradient(90deg, #c98a4a 0%, #3a3a3a 35%, #2b2b2b 65%, #6f9ac0 100%);
  }
  .feature {
    position: absolute; font-size: 7.5px; line-height: 9px; width: 62px;
  }
  .feature.left { left: 15px; }
  .feature.right { left: 349px; }
  .connectors { position: absolute; left: 0; top: 0; width: 418px; height: 592px; pointer-events: none; }
  .join-panel {
    position: absolute; left: 0; top: 438px; width: 418px; height: 154px;
    background: linear-gradient(180deg, var(--blue) 0%, var(--blue-deep) 100%);
  }
  .bubble-art {
    position: absolute; left: 226px; top: 412px; width: 200px; height: 190px;
    border-radius: 50% 0 0 50%; background: var(--yellow);
  }
  .bubble-art::after {
    content: ""; position: absolute; left: 40px; top: 46px; width: 116px; height: 116px;
    border-radius: 50%; background: var(--paper);
  }
  .join-title {
    position: absolute; left: 15px; top: 450px;
    font-family: "Bebas Neue", sans-serif; font-weight: 400; font-size: 19px; line-height: 22px;
    color: var(--paper); text-transform: uppercase; white-space: nowrap;
  }
  .benefits { position: absolute; left: 15px; top: 480px; width: 205px; list-style: none; }
  .benefits li {
    position: relative; padding-left: 14px; margin-bottom: 6px;
    font-size: 10.5px; line-height: 13px; color: var(--paper);
  }
  .benefits li::before {
    content: ""; position: absolute; left: 0; top: 2px; width: 5px; height: 5px;
    border: 2px solid var(--yellow); border-radius: 50%;
  }
</style>
</head>
<body>
<article class="advert">
  <svg class="header-band" viewBox="0 0 418 108" aria-hidden="true">
    <polygon points="124,0 418,0 418,104 151,104" fill="var(--blue)"/>
  </svg>
  <h1 class="headline">The oVex platform that is<br>community built, managed<br>and owned.</h1>
  <div class="brand"><span class="brand-dot"></span><span class="brand-name">AEROLUME</span></div>

  <p class="intro">The world has changed forever, disruption is inevitable and we are looking for the best talent to partner with us through our unique equity participation program.</p>

  <h2 class="community-band">The Aerolume community where:</h2>

  <div class="app-screens" role="img" aria-label="Three smartphone screens from the app: a video profile, the superpower selection menu and a video call"></div>

  <svg class="connectors" viewBox="0 0 418 592" aria-hidden="true">
    <g stroke="var(--line)" stroke-width="0.8" stroke-dasharray="1.5 1.5">
      <line x1="66" y1="259" x2="94" y2="259"/>
      <line x1="66" y1="297" x2="94" y2="297"/>
      <line x1="66" y1="339" x2="94" y2="339"/>
      <line x1="66" y1="383" x2="94" y2="383"/>
      <line x1="313" y1="256" x2="346" y2="256"/>
      <line x1="313" y1="294" x2="346" y2="294"/>
      <line x1="313" y1="336" x2="346" y2="336"/>
      <line x1="313" y1="380" x2="346" y2="380"/>
    </g>
    <g fill="var(--line)">
      <circle cx="66" cy="259" r="1.3"/><circle cx="66" cy="297" r="1.3"/>
      <circle cx="66" cy="339" r="1.3"/><circle cx="66" cy="383" r="1.3"/>
      <circle cx="346" cy="256" r="1.3"/><circle cx="346" cy="294" r="1.3"/>
      <circle cx="346" cy="336" r="1.3"/><circle cx="346" cy="380" r="1.3"/>
    </g>
  </svg>

  <p class="feature left" style="top:251px">Users are paid<br>for their data</p>
  <p class="feature left" style="top:284px">Platform 100%<br>Owned by the<br>users</p>
  <p class="feature left" style="top:326px">Democratised<br>Internet of the<br>future is built</p>
  <p class="feature left" style="top:370px">Decentralised<br>Technologies<br>are core</p>
  <p class="feature right" style="top:248px">Global Equality and<br>Fairness are enabled</p>
  <p class="feature right" style="top:281px">Privacy and<br>consent are<br>a right</p>
  <p class="feature right" style="top:323px">Individuals excel<br>and are empowered<br>by the community</p>
  <p class="feature right" style="top:367px">Marketing and<br>Advertising is<br>re-imagined</p>

  <div class="join-panel"></div>
  <div class="bubble-art" role="img" aria-label="Decorative cluster of yellow bubbles around a large white circle"></div>
  <h2 class="join-title">By joining our team you will be</h2>
  <ul class="benefits">
    <li>Instrumental in disrupting the digital world and how the Internet is used.</li>
    <li>Part of a dynamic, ground-breaking team</li>
    <li>Challenged and exhilarated</li>
    <li>Create substantial value for yourself and your community</li>
  </ul>
</article>
</body>
</html>
```